Business card design for holistic health care clinic

We need a double-sided business card design for our holistic health care clinic that integrates our logo design and also its color scheme. My business is called Veluma. It is an integrative medicine clinic. You have already done the logo for me. Please ensure an elegant and upscale design that is not cluttered, but still has all the necessary information (please see below for details).

Target Market(s)

Wellness, fitness, rehabilitation for educated, well-traveled open-minded clients who are focused on natural, organic, balanced and preventive healthcare and lifestyle.

Industry/Entity Type

Medical

Contact Information for Business Card

Modern, clean.

Number of Pages Required

1 page

Font styles to use
Serif
Sans Serif

Colors

Designer to choose colors to be used in the design.

Requirements
Must have
• Logo on one side, all other information on the other side.
• Other information should include:
• Tomas Brevik - DOE, CPT, LMT
• 4120 North Harlow Street
• Austin, TX 78631
• 512 608 2947
• 818 459 7208
• info@VelumaHealth.com
• t.brevik@VelumaHealth.com
Nice to have
• Darker background on front - but not totally black - shaded/dark gray.

```html
<!DOCTYPE html>
<html lang="en">
<head>
<meta charset="UTF-8">
<title>Veluma – Business Card</title>
<link href="https://fonts.googleapis.com/css2?family=Montserrat:wght@400;700;800&family=Raleway:wght@400;500&display=swap" rel="stylesheet">
<style>
  :root {
    --brand-blue: #1b8fd0;
    --brand-blue-dark: #1279b8;
    --ink-dark: #222325;
    --ink-grey: #6b6f74;
    --paper: #ffffff;
    --canvas-bg: #2b2d30;
  }
  * { margin: 0; padding: 0; box-sizing: border-box; }
  html, body {
    width: 1200px; height: 852px; overflow: hidden;
    background: var(--canvas-bg);
  }
  .canvas {
    width: 1200px; height: 852px;
    display: flex; flex-direction: column; align-items: center; justify-content: center;
    gap: 40px;
  }
  .card {
    position: relative;
    width: 640px; height: 366px;
    border-radius: 22px;
    overflow: hidden;
    box-shadow: 0 14px 30px rgba(0,0,0,.45);
  }

  /* Front */
  .card-front {
    background: var(--brand-blue);
    display: flex; align-items: center; justify-content: center;
  }
  .front-brand { text-align: center; color: var(--paper); }
  .brand-name {
    font-family: "Montserrat", sans-serif;
    font-weight: 800;
    font-size: 92px;
    letter-spacing: 2px;
    line-height: 1;
  }
  .brand-tagline {
    font-family: "Montserrat", sans-serif;
    font-weight: 700;
    font-size: 22px;
    margin-top: 10px;
    letter-spacing: .3px;
  }

  /* Back */
  .card-back { background: var(--paper); }
  .back-art { position: absolute; inset: 0; }
  .holder {
    position: absolute; right: 30px; top: 114px; text-align: right;
  }
  .holder-name {
    font-family: "Montserrat", sans-serif;
    font-weight: 700;
    font-size: 30px;
    color: var(--brand-blue);
    letter-spacing: -.5px;
    line-height: 30px;
  }
  .holder-title {
    font-family: "Raleway", sans-serif;
    font-size: 13px;
    line-height: 16px;
    color: var(--ink-grey);
    margin-top: 10px;
    letter-spacing: .5px;
  }
  .back-brand {
    position: absolute; left: 34px; top: 150px;
    color: var(--brand-blue);
  }
  .back-brand .brand-name { font-size: 62px; }
  .back-brand .brand-tagline { font-size: 15px; margin-top: 6px; text-align: left; }
  .contacts {
    position: absolute; left: 38px; top: 262px;
    list-style: none;
    font-family: "Raleway", sans-serif;
    font-size: 15px;
    color: var(--ink-dark);
  }
  .contacts li { display: flex; align-items: center; gap: 10px; height: 19px; }
  .contacts svg { width: 11px; height: 11px; flex: none; }
  .address {
    position: absolute; left: 306px; bottom: 0; height: 30px; width: 282px;
    display: flex; align-items: center; justify-content: center;
    font-family: "Raleway", sans-serif; font-size: 13px; color: var(--paper);
    white-space: nowrap;
  }
</style>
</head>
<body>
<main class="canvas">

  <section class="card card-front" aria-label="Card front">
    <div class="front-brand">
      <div class="brand-name">VELUMA</div>
      <div class="brand-tagline">Integrative Holistic Medicine</div>
    </div>
  </section>

  <section class="card card-back" aria-label="Card back">
    <svg class="back-art" width="640" height="366" viewBox="0 0 640 366">
      <path d="M250 0 C380 0 560 20 640 70 L640 0 Z" fill="var(--brand-blue)"/>
      <path d="M250 0 C380 0 560 20 640 70" fill="none" stroke="var(--ink-dark)" stroke-width="5"/>
      <line x1="330" y1="150" x2="612" y2="150" stroke="var(--brand-blue)" stroke-width="1"/>
      <line x1="30" y1="250" x2="300" y2="250" stroke="var(--brand-blue)" stroke-width="1"/>
      <rect x="0" y="354" width="306" height="12" fill="var(--brand-blue)"/>
      <rect x="306" y="336" width="282" height="30" fill="var(--ink-dark)"/>
      <rect x="594" y="336" width="46" height="30" fill="var(--brand-blue)"/>
    </svg>

    <div class="holder">
      <div class="holder-name">TOMAS BREVIK</div>
      <div class="holder-title">DOE, CPT, LMT</div>
    </div>

    <div class="back-brand">
      <div class="brand-name">VELUMA</div>
      <div class="brand-tagline">Integrative Holistic Medicine</div>
    </div>

    <ul class="contacts">
      <li>
        <svg viewBox="0 0 12 12"><path d="M3 1 L5 3.5 L4 5 Q5 7 7 8 L8.5 7 L11 9 L9.5 11 Q4 10.5 1 3 Z" fill="var(--brand-blue)"/></svg>
        512 608 2947
      </li>
      <li>
        <svg viewBox="0 0 12 12"><rect x="3" y="0.8" width="6" height="10.4" rx="1" fill="none" stroke="var(--brand-blue)" stroke-width="1.4"/><circle cx="6" cy="9.2" r=".7" fill="var(--brand-blue)"/></svg>
        818 459 7208
      </li>
      <li>
        <svg viewBox="0 0 12 12"><rect x="1" y="2.5" width="10" height="7" fill="none" stroke="var(--brand-blue)" stroke-width="1.3"/><path d="M1 2.5 L6 6.5 L11 2.5" fill="none" stroke="var(--brand-blue)" stroke-width="1.3"/></svg>
        info@VelumaHealth.com
      </li>
      <li>
        <svg viewBox="0 0 12 12"><circle cx="6" cy="6" r="5" fill="none" stroke="var(--brand-blue)" stroke-width="1.2"/><ellipse cx="6" cy="6" rx="2.2" ry="5" fill="none" stroke="var(--brand-blue)" stroke-width="1"/><line x1="1" y1="6" x2="11" y2="6" stroke="var(--brand-blue)" stroke-width="1"/></svg>
        t.brevik@VelumaHealth.com
      </li>
    </ul>

    <div class="address">4120 North Harlow Street Austin, TX 78631</div>
  </section>

</main>
</body>
</html>
```